Recipe mobile app, new flow and design for uploading recipe process

I need a new recipe upload process that's simple, intuitive, and engaging.
The goal is to have a user-friendly and fast flow.
The app is a social recipe library where anyone can upload a recipe after signing up. I currently have a flow, but it's "boring," so I'd like to significantly improve this aspect of the app.
When I create a new recipe, it's immediately saved and labeled as a draft. I'll then need to specify:
- Recipe title
- Cover image (required)
- Number of people (how many people is the recipe for)
- Ingredients (name, quantity, and unit of measurement)
- Recipe explanation (broken down into steps, and I can optionally attach an image to each step)
- Upload
Every change is immediately saved, so you can edit, exit, and resume editing later.
I've attached images of the app and the current upload process.
Thank you.
Low design quality
Good morning everyone,
some of the designs received are fantastic, but please make sure to carefully read the requirement so as not to do extra work.
The requirement is to redesign the flow that a user follows when uploading a recipe to the platform.
We have uploaded the current app screens to give you an idea of what the product looks like, what the colors and style are, but we don’t need a full redesign - only the part mentioned above, while keeping the existing style and colors (we cannot rework the entire theme).
To clarify: if you look at the screens shared in the zip file attached to the project, the focus should be on the screens from 5_.png to 10_.png.
These screens can be redesigned in the most creative way you think, as long as the overall theme remains unchanged.
Thank you for your attention.

```html
<!DOCTYPE html>
<html lang="en">
<head>
<meta charset="utf-8">
<title>Recipe App – Screen Flow</title>
<link href="https://fonts.googleapis.com/css2?family=Inter:wght@400;500;600;700&display=swap" rel="stylesheet">
<style>
:root{
  --board:#2fc46e;
  --primary:#1fcc79;
  --primary-soft:#e3fff1;
  --ink:#2e3e5c;
  --muted:#9fa5c0;
  --line:#d0dbea;
  --field:#f4f5f7;
  --keyboard:#d3d5db;
  --accent:#ff6464;
  --overlay:rgba(30,34,44,.55);
  --food-a:#c98a4b;
  --food-b:#6e7a3a;
}
*{box-sizing:border-box;margin:0;padding:0}
html,body{width:900px;height:1200px;overflow:hidden}
body{background:var(--board);font-family:"Inter",sans-serif;color:var(--ink);position:relative}
.screen{position:absolute;width:114px;height:248px;background:#fff;border-radius:9px;overflow:hidden;padding:16px 9px 0;font-size:5px;display:flex;flex-direction:column;gap:5px}
.status{position:absolute;top:4px;left:9px;right:9px;display:flex;justify-content:space-between;font-size:4.5px;font-weight:600}
.status .draft{color:var(--primary);font-weight:500}
.title{font-size:8px;font-weight:700;text-align:center}
.title.left{text-align:left}
.sub{color:var(--muted);text-align:center;font-size:4.6px;line-height:1.4}
.sub.left{text-align:left}
.field{height:15px;border:.6px solid var(--line);border-radius:8px;display:flex;align-items:center;padding:0 7px;color:var(--muted);font-size:4.6px;white-space:nowrap;overflow:hidden}
.field.filled{color:var(--ink);border-color:var(--primary)}
.field.sm{height:13px;padding:0 4px;justify-content:center}
.btn{height:15px;border-radius:8px;background:var(--primary);color:#fff;font-weight:600;display:flex;align-items:center;justify-content:center;font-size:5px}
.btn.alt{background:var(--accent)}
.btn.ghost{background:#fff;color:var(--ink);border:.6px solid var(--line)}
.btn.soft{background:var(--primary-soft);color:var(--primary);height:13px}
.link{text-align:center;font-size:4.6px;color:var(--muted)}
.link b{color:var(--primary)}
.codes{display:flex;justify-content:center;gap:5px}
.codes span{width:17px;height:17px;border:.6px solid var(--line);border-radius:5px;display:flex;align-items:center;justify-content:center;font-size:7px;font-weight:700}
.codes span.on{border-color:var(--primary)}
.kbd{position:absolute;left:0;right:0;bottom:0;height:78px;background:var(--keyboard);padding:6px 3px;display:flex;flex-direction:column;gap:4px}
.krow{height:12px;background:repeating-linear-gradient(90deg,#fff 0 9.2px,transparent 9.2px 10.8px);border-radius:2px}
.krow.mid{margin:0 5px}
.krow.low{margin:0 16px}
.krow.space{margin:0 26px;background:#fff}
.check{display:flex;gap:4px;align-items:center;color:var(--muted);font-size:4.6px}
.check i{width:7px;height:7px;border-radius:50%;background:var(--primary-soft);border:.6px solid var(--primary)}
.check i.on{background:var(--primary)}
.search{height:15px;border-radius:8px;background:var(--field);display:flex;align-items:center;gap:4px;padding:0 6px;color:var(--muted);font-size:4.6px}
.chips{display:flex;gap:4px}
.chip{padding:3px 7px;border-radius:8px;background:var(--field);color:var(--muted);font-size:4.6px}
.chip.on{background:var(--primary);color:#fff}
.grid{display:grid;grid-template-columns:1fr 1fr;gap:6px 5px}
.card .who{display:flex;align-items:center;gap:3px;font-size:4px;margin-bottom:2px}
.dot{width:7px;height:7px;border-radius:50%;background:#c8d1df;flex:none}
.photo{height:40px;border-radius:7px;background:linear-gradient(135deg,var(--food-a),var(--food-b))}
.photo.b{background:linear-gradient(135deg,#d6a35c,#8a4b2a)}
.photo.c{background:linear-gradient(135deg,#3c5a38,#a9a05a)}
.card .name{font-weight:700;font-size:5px;margin-top:2px}
.card .meta{color:var(--muted);font-size:4px}
.nav{position:absolute;bottom:0;left:0;right:0;height:20px;border-top:.6px solid #eef1f5;display:flex;justify-content:space-around;align-items:center;background:#fff}
.nav span{width:7px;height:7px;border-radius:2px;background:var(--muted)}
.nav span.on{background:var(--primary)}
.nav span.fab{width:15px;height:15px;border-radius:50%;background:var(--primary);margin-top:-10px}
.overlay{position:absolute;inset:0;background:var(--overlay)}
.sheet{position:absolute;left:0;right:0;bottom:0;background:#fff;border-radius:12px 12px 0 0;padding:8px 9px;display:flex;flex-direction:column;gap:5px}
.slider{height:3px;border-radius:2px;background:linear-gradient(90deg,var(--primary) 60%,var(--line) 60%)}
.row{display:flex;gap:5px}
.row>*{flex:1}
.avatar{width:34px;height:34px;border-radius:50%;background:radial-gradient(circle at 40% 35%,#e8b89a,#7a4a38);align-self:center}
.stats{display:flex;justify-content:space-around;text-align:center;font-size:4.5px;color:var(--muted)}
.stats b{display:block;color:var(--ink);font-size:6px}
.tabs{display:flex;border-bottom:.6px solid var(--line)}
.tabs span{flex:1;text-align:center;padding-bottom:3px;color:var(--muted)}
.tabs span.on{color:var(--ink);font-weight:600;border-bottom:1.5px solid var(--primary)}
.cover{height:56px;border:.8px dashed var(--line);border-radius:8px;display:flex;flex-direction:column;align-items:center;justify-content:center;gap:3px;color:var(--muted);flex:none}
.label{font-weight:600;font-size:5.4px;display:flex;justify-content:space-between;align-items:center}
.label small{font-weight:400;font-size:4.2px;color:var(--muted)}
.area{height:30px;border:.6px solid var(--line);border-radius:8px;padding:5px 7px;color:var(--muted);flex:none}
.stepper{display:flex;align-items:center;justify-content:space-between;height:15px;border:.6px solid var(--line);border-radius:8px;padding:0 3px}
.stepper span{width:10px;height:10px;border-radius:50%;background:var(--primary-soft);color:var(--primary);display:flex;align-items:center;justify-content:center;font-weight:700;font-size:6px}
.stepper b{font-size:5px}
.ingrow{display:grid;grid-template-columns:1fr 17px 17px;gap:3px}
.step{display:flex;gap:4px;border:.6px solid var(--line);border-radius:8px;padding:4px;align-items:flex-start}
.step .num{width:9px;height:9px;border-radius:50%;background:var(--primary);color:#fff;font-size:4.4px;font-weight:700;display:flex;align-items:center;justify-content:center;flex:none}
.step p{flex:1;color:var(--muted);font-size:4.4px;line-height:1.4}
.step .pic{width:18px;height:18px;border:.6px dashed var(--line);border-radius:4px;color:var(--muted);display:flex;align-items:center;justify-content:center;font-size:7px;flex:none}
.ing{display:flex;align-items:center;gap:4px;font-size:4.6px}
.ing i{width:8px;height:8px;border-radius:50%;background:var(--primary-soft);flex:none}
.ing i.on{background:var(--primary)}
.modal{position:absolute;left:13px;right:13px;top:72px;background:#fff;border-radius:10px;padding:10px 8px;display:flex;flex-direction:column;align-items:center;gap:5px;text-align:center}
.emoji{width:34px;height:34px;border-radius:50%;background:radial-gradient(circle at 45% 40%,#ffd66b,#f2a53a)}
.hero{position:absolute;inset:0;background:linear-gradient(160deg,#e9d9b8,#c7843e 45%,#6f8a3a)}
.detail-img{height:44px;border-radius:7px;background:linear-gradient(135deg,#b97a3c,#5f7b34)}
.rule{height:.6px;background:var(--line);flex:none}
.foot{position:absolute;left:9px;right:9px;bottom:12px}
</style>
</head>
<body>

<!-- Row 1: onboarding and sign-in -->
<section class="screen" style="left:21px;top:30px">
  <div class="status"><span>9:41</span><span>●●●</span></div>
  <div role="img" aria-label="Illustration of plated dishes arranged in a circle" style="height:100px;border-radius:50%;background:radial-gradient(circle,#f4e6cf 30%,#c7924f 60%,#fff 61%)"></div>
  <div class="title">Start Cooking</div>
  <div class="sub">Join our community to cook better food and share it!</div>
  <div style="flex:1"></div>
  <div class="btn" style="margin-bottom:16px">Get Started</div>
</section>

<section class="screen" style="left:145px;top:30px">
  <div class="status"><span>9:41</span><span>●●●</span></div>
  <div class="title" style="margin-top:8px">Welcome Back!</div>
  <div class="sub">Please enter your account here</div>
  <div class="field">Email or phone number</div>
  <div class="field">Password</div>
  <div class="link" style="text-align:right">Forgot password?</div>
  <div class="btn">Login</div>
  <div class="link">Or continue with</div>
  <div class="btn alt">Quick Sign In</div>
  <div class="link">Don't have any account? <b>Sign Up</b></div>
</section>

<section class="screen" style="left:269px;top:30px">
  <div class="status"><span>9:41</span><span>●●●</span></div>
  <div class="title" style="margin-top:4px">Welcome!</div>
  <div class="sub">Please enter your account here</div>
  <div class="field filled">Email or phone number</div>
  <div class="field">Password</div>
  <div class="check"><i class="on"></i>At least 6 characters</div>
  <div class="check"><i></i>Contains a number</div>
  <div class="btn">Sign Up</div>
  <div class="kbd"><div class="krow"></div><div class="krow mid"></div><div class="krow low"></div><div class="krow space"></div></div>
</section>

<section class="screen" style="left:393px;top:30px">
  <div class="status"><span>9:41</span><span>●●●</span></div>
  <div class="title" style="margin-top:4px">Check your email</div>
  <div class="sub">We've sent the code to your email</div>
  <div class="codes"><span class="on">8</span><span>2</span><span></span><span></span></div>
  <div class="sub">code expires in: <b style="color:var(--accent)">03:12</b></div>
  <div class="btn">Verify</div>
  <div class="btn ghost">Send again</div>
  <div class="kbd"><div class="krow"></div><div class="krow mid"></div><div class="krow low"></div><div class="krow space"></div></div>
</section>

<section class="screen" style="left:517px;top:30px">
  <div class="status"><span>9:41</span><span>●●●</span></div>
  <div class="title" style="margin-top:4px">Check your email</div>
  <div class="sub">We've sent the code to your email</div>
  <div class="codes"><span class="on">8</span><span class="on">2</span><span class="on">6</span><span class="on">4</span></div>
  <div class="sub">code expires in: <b style="color:var(--accent)">02:48</b></div>
  <div class="btn">Verify</div>
  <div class="btn ghost">Send again</div>
  <div class="kbd"><div class="krow"></div><div class="krow mid"></div><div class="krow low"></div><div class="krow space"></div></div>
</section>

<section class="screen" style="left:641px;top:30px">
  <div class="status"><span>9:41</span><span>●●●</span></div>
  <div class="title" style="margin-top:4px">Check your email</div>
  <div class="sub">We've sent the code to your email</div>
  <div class="codes"><span class="on">8</span><span class="on">2</span><span class="on">6</span><span class="on">4</span></div>
  <div class="sub">code expires in: <b style="color:var(--accent)">02:10</b></div>
  <div class="btn">Verify</div>
  <div class="btn ghost">Send again</div>
</section>

<section class="screen" style="left:765px;top:30px">
  <div class="status"><span>9:41</span><span>●●●</span></div>
  <div class="title" style="margin-top:4px">Reset your password</div>
  <div class="sub">Please enter your new password</div>
  <div class="field filled">New password</div>
  <div class="label">Your password must contain:</div>
  <div class="check"><i class="on"></i>At least 6 characters</div>
  <div class="check"><i class="on"></i>Contains a number</div>
  <div class="btn" style="margin-top:6px">Done</div>
</section>

<!-- Row 2: home, search, filter -->
<section class="screen" style="left:21px;top:324px">
  <div class="status"><span>9:41</span><span>●●●</span></div>
  <div class="search">⌕ Search</div>
  <div class="label">Category</div>
  <div class="chips"><span class="chip on">All</span><span class="chip">Food</span><span class="chip">Drink</span></div>
  <div class="tabs"><span class="on">Left</span><span>Right</span></div>
  <div class="grid">
    <div class="card"><div class="who"><i class="dot"></i>Calum</div><div class="photo" role="img" aria-label="Pancake dish photo"></div><div class="name">Pancake</div><div class="meta">Food · &gt;60 mins</div></div>
    <div class="card"><div class="who"><i class="dot"></i>Elena</div><div class="photo b" role="img" aria-label="Salad dish photo"></div><div class="name">Salad</div><div class="meta">Food · &gt;60 mins</div></div>
  </div>
  <div class="nav"><span class="on"></span><span></span><span class="fab"></span><span></span><span></span></div>
</section>

<section class="screen" style="left:145px;top:324px">
  <div class="status"><span>9:41</span><span>●●●</span></div>
  <div class="row"><div class="search" style="flex:4">⌕ Pasta</div><div class="search" style="flex:1">≡</div></div>
  <div class="label">Search history</div>
  <div class="sub left">◷ Pancakes</div>
  <div class="sub left">◷ Salad</div>
  <div class="label">Search suggestions</div>
  <div class="chips"><span class="chip">sushi</span><span class="chip">sandwich</span></div>
  <div class="chips"><span class="chip">seafood</span><span class="chip">fried rice</span></div>
  <div class="kbd"><div class="krow"></div><div class="krow mid"></div><div class="krow low"></div><div class="krow space"></div></div>
</section>

<section class="screen" style="left:269px;top:324px">
  <div class="status"><span>9:41</span><span>●●●</span></div>
  <div class="search">⌕ Search</div>
  <div class="overlay"></div>
  <div class="sheet">
    <div class="title">Add a Filter</div>
    <div class="label">Category</div>
    <div class="chips"><span class="chip on">All</span><span class="chip">Food</span><span class="chip">Drink</span></div>
    <div class="label" style="justify-content:flex-start;gap:2px">Cooking Duration <small>(in minutes)</small></div>
    <div class="slider"></div>
    <div class="row"><div class="btn ghost">Cancel</div><div class="btn">Done</div></div>
  </div>
</section>

<section class="screen" style="left:393px;top:324px">
  <div class="status"><span>9:41</span><span>●●●</span></div>
  <div class="row"><div class="search" style="flex:4">⌕ Pasta</div><div class="search" style="flex:1">≡</div></div>
  <div class="grid">
    <div class="card"><div class="who"><i class="dot"></i>James</div><div class="photo" role="img" aria-label="Pasta dish photo"></div><div class="name">Pasta</div><div class="meta">Food · 40 mins</div></div>
    <div class="card"><div class="who"><i class="dot"></i>Anna</div><div class="photo c" role="img" aria-label="Pasta bowl photo"></div><div class="name">Pasta Bowl</div><div class="meta">Food · 30 mins</div></div>
    <div class="card"><div class="who"><i class="dot"></i>Lucas</div><div class="photo b" role="img" aria-label="Noodle dish photo"></div><div class="name">Noodles</div><div class="meta">Food · 25 mins</div></div>
    <div class="card"><div class="who"><i class="dot"></i>Mia</div><div class="photo" role="img" aria-label="Baked pasta photo"></div><div class="name">Baked Pasta</div><div class="meta">Food · 50 mins</div></div>
  </div>
</section>

<!-- Row 3: profiles -->
<section class="screen" style="left:21px;top:612px">
  <div class="status"><span>9:41</span><span>●●●</span></div>
  <div class="avatar" role="img" aria-label="Profile photo"></div>
  <div class="title">Chiara Ferri</div>
  <div class="stats"><span><b>32</b>Recipes</span><span><b>782</b>Following</span><span><b>1.287</b>Followers</span></div>
  <div class="tabs"><span class="on">Recipes</span><span>Liked</span></div>
  <div class="grid">
    <div class="card"><div class="photo" role="img" aria-label="Dish photo"></div><div class="name">Pancake</div></div>
    <div class="card"><div class="photo c" role="img" aria-label="Dish photo"></div><div class="name">Salad</div></div>
  </div>
  <div class="nav"><span></span><span></span><span class="fab"></span><span></span><span class="on"></span></div>
</section>

<section class="screen" style="left:145px;top:612px">
  <div class="status"><span>9:41</span><span>●●●</span></div>
  <div class="avatar" role="img" aria-label="Profile photo" style="background:radial-gradient(circle at 40% 35%,#d9a98a,#4a3028)"></div>
  <div class="title">Marco Rossi</div>
  <div class="btn" style="width:50px;align-self:center;height:12px">Follow</div>
  <div class="stats"><span><b>24</b>Recipes</span><span><b>310</b>Following</span><span><b>968</b>Followers</span></div>
  <div class="tabs"><span class="on">Recipes</span><span>Liked</span></div>
  <div class="grid">
    <div class="card"><div class="photo b" role="img" aria-label="Dish photo"></div><div class="name">Risotto</div></div>
    <div class="card"><div class="photo" role="img" aria-label="Dish photo"></div><div class="name">Lasagna</div></div>
  </div>
</section>

<section class="screen" style="left:269px;top:612px">
  <div class="status"><span>9:41</span><span>●●●</span></div>
  <div class="title">Liked</div>
  <div class="grid">
    <div class="card"><div class="photo" role="img" aria-label="Dish photo"></div><div class="name">Pancake</div><div class="meta">Food · 60 mins</div></div>
    <div class="card"><div class="photo c" role="img" aria-label="Dish photo"></div><div class="name">Salad</div><div class="meta">Food · 20 mins</div></div>
    <div class="card"><div class="photo b" role="img" aria-label="Dish photo"></div><div class="name">Curry</div><div class="meta">Food · 45 mins</div></div>
    <div class="card"><div class="photo" role="img" aria-label="Dish photo"></div><div class="name">Omelette</div><div class="meta">Food · 15 mins</div></div>
  </div>
  <div class="nav"><span></span><span></span><span class="fab"></span><span class="on"></span><span></span></div>
</section>

<!-- Row 4: recipe upload flow and detail -->
<section class="screen" style="left:21px;top:900px">
  <div class="status"><span>Cancel</span><span class="draft">✓ Draft saved</span><span>1/2</span></div>
  <div class="cover"><span style="font-size:10px">▣</span><b style="color:var(--ink)">Add Cover Photo</b><span>(required, up to 12 Mb)</span></div>
  <div class="label">Recipe Title</div>
  <div class="field">Enter recipe title</div>
  <div class="label">Servings <small>people</small></div>
  <div class="stepper"><span>−</span><b>4 people</b><span>+</span></div>
  <div class="label">Description</div>
  <div class="area">Tell a little about your food</div>
  <div class="btn foot">Next</div>
</section>

<section class="screen" style="left:145px;top:900px">
  <div class="status"><span>Cancel</span><span class="draft">✓ Draft saved</span><span>2/2</span></div>
  <div class="label">Ingredients <small>name · qty · unit</small></div>
  <div class="ingrow"><div class="field sm filled" style="justify-content:flex-start">Flour</div><div class="field sm filled">250</div><div class="field sm filled">g</div></div>
  <div class="ingrow"><div class="field sm" style="justify-content:flex-start">Name</div><div class="field sm">Qty</div><div class="field sm">Unit</div></div>
  <div class="btn soft">+ Ingredient</div>
  <div class="rule"></div>
  <div class="label">Steps</div>
  <div class="step"><span class="num">1</span><p>Mix flour and eggs in a bowl until smooth</p><span class="pic" role="img" aria-label="Add optional step photo">+</span></div>
  <div class="btn soft">+ Step</div>
  <div class="row foot"><div class="btn ghost">Back</div><div class="btn">Upload</div></div>
</section>

<section class="screen" style="left:269px;top:900px">
  <div class="status"><span>9:41</span><span>●●●</span></div>
  <div class="overlay"></div>
  <div class="modal">
    <div class="emoji" role="img" aria-label="Celebrating smiley illustration"></div>
    <div class="title">Upload Success</div>
    <div class="sub">Your recipe has been uploaded, you can see it on your profile</div>
    <div class="btn" style="align-self:stretch">Back to Home</div>
  </div>
</section>

<section class="screen" style="left:393px;top:900px;padding:0">
  <div class="hero" role="img" aria-label="Full-screen photo of a finished dish with vegetables"></div>
</section>

<section class="screen" style="left:517px;top:900px">
  <div class="status"><span>9:41</span><span>●●●</span></div>
  <div class="title left">Cacao Maca Walnut</div>
  <div class="meta" style="color:var(--muted)">Food · 60 mins · 4 people</div>
  <div class="row" style="align-items:center"><div style="display:flex;gap:3px;align-items:center"><i class="dot"></i>Elena</div><div class="chip on" style="flex:0">Like</div></div>
  <div class="rule"></div>
  <div class="label">Description</div>
  <div class="sub left">A soft cacao cake with walnuts, ready in one hour.</div>
  <div class="label">Ingredients</div>
  <div class="ing"><i class="on"></i>4 pcs Eggs</div>
  <div class="ing"><i class="on"></i>100 g Butter</div>
  <div class="ing"><i></i>1/2 cup Sugar</div>
  <div class="label">Steps</div>
  <div class="detail-img" role="img" aria-label="Step photo of ingredients in a bowl"></div>
</section>

</body>
</html>
```